Vormi Sauce. Co Label Design Refresh

We need a new label design for an All-Purpose Chili Oil Sauce company based in Southern California. Vormi Sauce is an Asian American family-oriented company. Our sauces are curated in small batches using premium, fresh, sustainable ingredients. All sauces are GF, contain no refined sugars, no msg, no preservatives. Vormi Sauce is not limited, but is great for dipping, topping, marinades, and stir-fry etc. We would like to emphasize that most of our products are Organic, we are currently working on getting all of our products Organic certified. The company is established and is looking to revamp the label. I have attached the following for reference, the redesign brief from our graphic designer who is currently working on revamping our website, Vormi Sauce sales sheet, and the Vormi Sauce website link below,
https://www.vormisauce.example/

Target Market(s)

Similar target to Brightfield customer. The target customers for Brightfield Grocers are individuals and families whose income is well above the national average, lead a healthy lifestyle and conscious of environment. Most of the customers have college degrees and live in upscale sub-urban or metropolitan areas. Another target group of Brightfield are wealthy customers.

Industry/Entity Type

CPG

Requirements
Must have
• Emphasis on healthiest, natural and organic foods.

```html
<!DOCTYPE html>
<html lang="en">
<head>
<meta charset="utf-8">
<title>Vormi Sauce Label Set</title>
<link rel="stylesheet" href="https://fonts.googleapis.com/css2?family=Rubik+Dirt&family=Staatliches&family=Saira+Condensed:wght@600;700&family=Libre+Franklin:wght@400;700;900&display=swap">
<style>
:root{
  --red:#c8202f;
  --white:#ffffff;
  --ink:#111111;
  --backdrop:#eceef0;
  --display:"Rubik Dirt", Impact, sans-serif;
  --stamp:"Staatliches", Impact, sans-serif;
  --condensed:"Saira Condensed", "Arial Narrow", sans-serif;
  --plain:"Libre Franklin", Arial, sans-serif;
}
*{box-sizing:border-box;margin:0;padding:0}
html,body{width:1200px;height:1200px;overflow:hidden}
body{background:var(--backdrop);position:relative;font-family:var(--plain)}

.label{position:absolute;background:var(--white);overflow:hidden;box-shadow:0 2px 6px rgba(0,0,0,.18)}
.label-wide{left:28px;top:24px;width:756px;height:383px}
.label-front{width:255px;height:368px;left:28px}
.label-front.first{top:424px}
.label-front.second{top:815px}

.red-band{position:absolute;left:0;right:0;bottom:0;background:var(--red)}
.label-wide .red-band{height:100px}
.label-front .red-band{height:106px}

.skyline{position:absolute;background:linear-gradient(to bottom,rgba(200,32,47,.15),rgba(200,32,47,.6) 55%,var(--red))}
.label-wide .skyline{left:241px;top:190px;width:292px;height:95px}
.label-front .skyline{left:10px;top:182px;width:235px;height:82px}

.brand{position:absolute;color:var(--red);font-family:var(--stamp);font-weight:400;text-align:center;line-height:.9;letter-spacing:2px}
.label-wide .brand{left:268px;top:36px;width:218px;font-size:60px}
.label-front .brand{left:18px;top:30px;width:219px;font-size:60px}
.brand-mark{display:inline-block;width:14px;height:14px;background:var(--red);margin-bottom:6px}

.heat-meter{position:absolute;border:2px solid var(--red);border-radius:5px;display:flex;align-items:center;gap:6px;padding:0 8px;color:var(--red);font-family:var(--stamp);font-size:13px;letter-spacing:.5px;height:20px}
.label-wide .heat-meter{left:289px;top:156px;width:176px}
.label-front .heat-meter{left:45px;top:150px;width:170px;height:19px}
.heat-meter svg{width:86px;height:12px}

.badges{position:absolute;display:flex;gap:4px}
.label-wide .badges{left:273px;top:299px}
.label-front .badges{left:30px;top:286px}
.badge{width:35px;height:52px;border:2px solid var(--white);border-radius:5px;display:flex;flex-direction:column;align-items:center;padding-top:4px;color:var(--white);font-family:var(--stamp);font-size:7px;line-height:1;text-align:center}
.badge svg{width:24px;height:24px;margin-bottom:4px}

.tagline{position:absolute;color:var(--white);font-family:var(--condensed);font-weight:700;font-size:15px;letter-spacing:.4px;white-space:nowrap;text-align:center}
.label-wide .tagline{left:241px;top:356px;width:292px}
.label-front .tagline{left:0;top:343px;width:255px}

.nutrition{position:absolute;left:23px;top:26px;width:191px;height:252px;border:1px solid var(--ink);padding:2px 3px;color:var(--ink);font-size:6.5px;line-height:1.35;overflow:hidden}
.nutrition h2{font-weight:900;font-size:16px;line-height:1;border-bottom:1px solid var(--ink);padding-bottom:1px}
.nutrition .row{display:flex;justify-content:space-between}
.nutrition .bold{font-weight:700}
.nutrition .thick{border-bottom:5px solid var(--ink)}
.nutrition .mid{border-bottom:3px solid var(--ink)}
.nutrition .line{border-bottom:.5px solid var(--ink)}
.nutrition .calories{font-weight:900;font-size:13px;line-height:1.1}
.nutrition .indent{padding-left:10px}
.nutrition .indent2{padding-left:22px}
.nutrition .foot{font-size:4.4px;line-height:1.15;margin-top:2px}

.ingredients{position:absolute;left:23px;top:288px;width:168px;color:var(--white);font-family:var(--stamp);font-size:5.3px;line-height:1.4;letter-spacing:.1px}
.ingredients h3{font-weight:400;font-size:5.5px;margin-bottom:8px}

.variety{position:absolute;left:534px;top:20px;width:194px;color:var(--red);text-align:center;font-family:var(--condensed);font-weight:700;font-size:12px;line-height:1}
.variety small{display:block;font-size:8px;font-weight:600}
.rule{position:absolute;left:534px;width:194px;height:3px;background:var(--red)}
.rule.top{top:47px}
.rule.bottom{top:346px;background:var(--white)}

.headline{position:absolute;left:534px;width:194px;display:flex;justify-content:center;color:var(--red);font-family:var(--display);line-height:1;white-space:nowrap}
.headline span{flex-shrink:0;display:inline-block;transform-origin:center}
.headline.mild{top:52px;font-size:70px}
.headline.mild span{transform:scaleX(1)}
.headline.chilli{top:118px;font-size:66px}
.headline.chilli span{transform:scaleX(.78)}
.headline.sauce{top:182px;font-size:62px}
.headline.sauce span{transform:scaleX(.86)}
.headline.caution{top:240px;font-size:38px;font-family:var(--stamp);letter-spacing:1px}
.headline.needed{top:286px;font-size:50px;color:var(--white)}
.headline.needed span{transform:scaleX(.9)}
.distributor{position:absolute;left:534px;top:356px;width:194px;text-align:center;color:var(--white);font-size:4.4px;line-height:1.4;font-weight:700}
</style>
</head>
<body>

<section class="label label-wide">
  <div class="red-band"></div>

  <div class="nutrition">
    <h2>Nutrition Facts</h2>
    <div>16 servings per container</div>
    <div class="row bold thick"><span>Serving size</span><span>1 Tablespoon (16g)</span></div>
    <div class="bold" style="font-size:5.5px">Amount Per Serving</div>
    <div class="row calories mid"><span>Calories</span><span style="font-size:15px">90</span></div>
    <div class="row line" style="justify-content:flex-end;font-size:5px"><span>% Daily Value*</span></div>
    <div class="row line"><span><b>Total Fat</b> 8g</span><b>12%</b></div>
    <div class="row line indent"><span>Saturated Fat 1g</span><b>4%</b></div>
    <div class="row line indent"><span><i>Trans</i> Fat 0g</span><span></span></div>
    <div class="row line"><span><b>Cholesterol</b> 0mg</span><b>0%</b></div>
    <div class="row line"><span><b>Sodium</b> 280mg</span><b>12%</b></div>
    <div class="row line"><span><b>Total Carbohydrate</b> 3g</span><b>1%</b></div>
    <div class="row line indent"><span>Dietary Fiber 0g</span><b>0%</b></div>
    <div class="row line indent"><span>Total Sugars 1g</span><span></span></div>
    <div class="row line indent2"><span>Includes 1g Added Sugars</span><b>2%</b></div>
    <div class="row thick"><span><b>Protein</b> 1g</span><b>2%</b></div>
    <div class="row line"><span>Vitamin D 0mcg</span><span>0%</span></div>
    <div class="row line"><span>Calcium 0mg</span><span>0%</span></div>
    <div class="row line"><span>Iron 0.36mg</span><span>2%</span></div>
    <div class="row line"><span>Potassium 0mg</span><span>0%</span></div>
    <div class="row line"><span>Vitamin A</span><span>2%</span></div>
    <div class="row mid"><span>Vitamin C</span><span>2%</span></div>
    <div class="foot">*The % Daily Value (DV) tells you how much a nutrient in a serving of food contributes to a daily diet. 2,000 calories a day is used for general nutrition advice.</div>
  </div>

  <div class="ingredients">
    <h3>INGREDIENTS:</h3>
    SUNFLOWER OIL*, ORGANIC GLUTEN FREE TAMARI SOY SAUCE (WATER, ORGANIC SOYBEANS, SALT, ORGANIC ALCOHOL), WATER, DRIED ONION, DRIED GARLIC, FERMENTED BLACK BEAN* (SOYBEAN, SALT), TOMATO PASTE, AND SALT. CONTAINS LESS THAN 2% OF EACH OF THE FOLLOWING: BACON (PORK, SEA SALT, RAW SUGAR, SPICES), DRIED GARBANZO BEAN, ORGANIC CANE SUGAR, SPICES, DRIED CHILI PEPPER, RED CHILI PEPPER POWDER, DRIED GINGER, GROUND SESAME SEED PASTE, SESAME OIL, DISTILLED VINEGAR*, DRIED SHRIMP*, AND LICORICE POWDER. *NON-GMO<br>
    ALLERGENS: CONTAINS SOYBEAN, SHELLFISH AND SESAME SEED
  </div>

  <div class="brand">VORMI<br>SAUCE <span class="brand-mark"></span></div>
  <div class="heat-meter">MEDIUM
    <svg viewBox="0 0 86 12"><g fill="#c8202f" stroke="#c8202f" stroke-width="1.2"><ellipse cx="7" cy="6" rx="3" ry="5" transform="rotate(25 7 6)"/><ellipse cx="22" cy="6" rx="3" ry="5" transform="rotate(25 22 6)"/><ellipse cx="37" cy="6" rx="3" ry="5" transform="rotate(25 37 6)"/></g><g fill="none" stroke="#c8202f" stroke-width="1.2"><ellipse cx="52" cy="6" rx="3" ry="5" transform="rotate(25 52 6)"/><ellipse cx="67" cy="6" rx="3" ry="5" transform="rotate(25 67 6)"/><ellipse cx="81" cy="6" rx="3" ry="5" transform="rotate(25 81 6)"/></g></svg>
  </div>
  <div class="skyline" role="img" aria-label="Silhouette of palm trees over a hillside city skyline"></div>
  <div class="badges">
    <div class="badge"><svg viewBox="0 0 24 24" fill="none" stroke="#fff" stroke-width="1.6"><circle cx="12" cy="12" r="10"/><path d="M12 6v13M9 9l3 3 3-3M9 13l3 3 3-3"/></svg>NO<br>GLUTEN</div>
    <div class="badge"><svg viewBox="0 0 24 24" fill="none" stroke="#fff" stroke-width="1.6"><circle cx="12" cy="12" r="10"/></svg>NO<br>GMO</div>
    <div class="badge"><svg viewBox="0 0 24 24" fill="none" stroke="#fff" stroke-width="1.6"><circle cx="12" cy="12" r="10"/><path d="M5 5l14 14"/></svg>NO<br>MSG</div>
    <div class="badge"><svg viewBox="0 0 24 24" fill="none" stroke="#fff" stroke-width="1.6"><circle cx="12" cy="12" r="10"/><path d="M10 6v5l-4 7h12l-4-7V6"/></svg>NO<br>PRESERVATION</div>
    <div class="badge"><svg viewBox="0 0 24 24"><circle cx="12" cy="12" r="10" fill="#fff"/><path d="M4 9h16M3 13h18M4 17h16" stroke="#c8202f" stroke-width="1.5"/></svg>MADE<br>IN USA</div>
  </div>
  <div class="tagline">Healthiest, Natural and Organic Foods</div>

  <div class="variety">Traditional - Medium<small>Made with Bacon and Shrimp</small></div>
  <div class="rule top"></div>
  <div class="headline mild"><span>MILD</span></div>
  <div class="headline chilli"><span>CHILLI</span></div>
  <div class="headline sauce"><span>SAUCE</span></div>
  <div class="headline caution"><span>NO CAUTION</span></div>
  <div class="headline needed"><span>NEEDED</span></div>
  <div class="rule bottom"></div>
  <div class="distributor">Distributed by: Meridel Foods<br>Pasadena, CA 91101 · Telephone: (555) 010-0148<br>E-mail: sales@vormisauce.example · Website: www.vormisauce.example</div>
</section>

<section class="label label-front first">
  <div class="red-band"></div>
  <div class="brand">VORMI<br>SAUCE <span class="brand-mark"></span></div>
  <div class="heat-meter">MEDIUM
    <svg viewBox="0 0 86 12"><g fill="#c8202f" stroke="#c8202f" stroke-width="1.2"><ellipse cx="7" cy="6" rx="3" ry="5" transform="rotate(25 7 6)"/><ellipse cx="22" cy="6" rx="3" ry="5" transform="rotate(25 22 6)"/><ellipse cx="37" cy="6" rx="3" ry="5" transform="rotate(25 37 6)"/></g><g fill="none" stroke="#c8202f" stroke-width="1.2"><ellipse cx="52" cy="6" rx="3" ry="5" transform="rotate(25 52 6)"/><ellipse cx="67" cy="6" rx="3" ry="5" transform="rotate(25 67 6)"/><ellipse cx="81" cy="6" rx="3" ry="5" transform="rotate(25 81 6)"/></g></svg>
  </div>
  <div class="skyline" role="img" aria-label="Silhouette of palm trees over a hillside city skyline"></div>
  <div class="badges">
    <div class="badge"><svg viewBox="0 0 24 24" fill="none" stroke="#fff" stroke-width="1.6"><circle cx="12" cy="12" r="10"/><path d="M12 6v13M9 9l3 3 3-3M9 13l3 3 3-3"/></svg>NO<br>GLUTEN</div>
    <div class="badge"><svg viewBox="0 0 24 24" fill="none" stroke="#fff" stroke-width="1.6"><circle cx="12" cy="12" r="10"/></svg>NO<br>GMO</div>
    <div class="badge"><svg viewBox="0 0 24 24" fill="none" stroke="#fff" stroke-width="1.6"><circle cx="12" cy="12" r="10"/><path d="M5 5l14 14"/></svg>NO<br>MSG</div>
    <div class="badge"><svg viewBox="0 0 24 24" fill="none" stroke="#fff" stroke-width="1.6"><circle cx="12" cy="12" r="10"/><path d="M10 6v5l-4 7h12l-4-7V6"/></svg>NO<br>PRESERVATION</div>
    <div class="badge"><svg viewBox="0 0 24 24"><circle cx="12" cy="12" r="10" fill="#fff"/><path d="M4 9h16M3 13h18M4 17h16" stroke="#c8202f" stroke-width="1.5"/></svg>MADE<br>IN USA</div>
  </div>
  <div class="tagline">Healthiest, Natural and Organic Foods</div>
</section>

<section class="label label-front second">
  <div class="red-band"></div>
  <div class="brand">VORMI<br>SAUCE <span class="brand-mark"></span></div>
  <div class="heat-meter">MEDIUM
    <svg viewBox="0 0 86 12"><g fill="#c8202f" stroke="#c8202f" stroke-width="1.2"><ellipse cx="7" cy="6" rx="3" ry="5" transform="rotate(25 7 6)"/><ellipse cx="22" cy="6" rx="3" ry="5" transform="rotate(25 22 6)"/><ellipse cx="37" cy="6" rx="3" ry="5" transform="rotate(25 37 6)"/></g><g fill="none" stroke="#c8202f" stroke-width="1.2"><ellipse cx="52" cy="6" rx="3" ry="5" transform="rotate(25 52 6)"/><ellipse cx="67" cy="6" rx="3" ry="5" transform="rotate(25 67 6)"/><ellipse cx="81" cy="6" rx="3" ry="5" transform="rotate(25 81 6)"/></g></svg>
  </div>
  <div class="skyline" role="img" aria-label="Silhouette of palm trees over a hillside city skyline"></div>
  <div class="badges">
    <div class="badge"><svg viewBox="0 0 24 24" fill="none" stroke="#fff" stroke-width="1.6"><circle cx="12" cy="12" r="10"/><path d="M12 6v13M9 9l3 3 3-3M9 13l3 3 3-3"/></svg>NO<br>GLUTEN</div>
    <div class="badge"><svg viewBox="0 0 24 24" fill="none" stroke="#fff" stroke-width="1.6"><circle cx="12" cy="12" r="10"/></svg>NO<br>GMO</div>
    <div class="badge"><svg viewBox="0 0 24 24" fill="none" stroke="#fff" stroke-width="1.6"><circle cx="12" cy="12" r="10"/><path d="M5 5l14 14"/></svg>NO<br>MSG</div>
    <div class="badge"><svg viewBox="0 0 24 24" fill="none" stroke="#fff" stroke-width="1.6"><circle cx="12" cy="12" r="10"/><path d="M10 6v5l-4 7h12l-4-7V6"/></svg>NO<br>PRESERVATION</div>
    <div class="badge"><svg viewBox="0 0 24 24"><circle cx="12" cy="12" r="10" fill="#fff"/><path d="M4 9h16M3 13h18M4 17h16" stroke="#c8202f" stroke-width="1.5"/></svg>MADE<br>IN USA</div>
  </div>
  <div class="tagline">Healthiest, Natural and Organic Foods</div>
</section>

</body>
</html>
```